Business card for Full Stable Works Vanhoorne

I would like to have me designed an professional business card with my existing logo for my company called : full stable works vanhoorne gcv.
I prefer a two sided business card with on the back side only the horses head and the website : fswvanhoorne-example.eu
Only one colour shouldbe all right.
The logo must appear in a nic professional way on the business card.

Other suggestion are welcome.

All copy wrights must be released by the designer after we have selected a final design.

Target Market(s)

Equestrian businesses

Industry/Entity Type

Business

Contact Information for Business Card

Gerard Vanhoorne
Title: zaakvoerder
Full Stable Works Vanhoorne GCV
Lindekouter 47
B - 9999 Voorbeeldegem
België
Phone: + 32 400 98 76 10
Mail: gerard@fswvanhoorne-example.eu

Font styles to use
Serif

Requirements
Must have
• My own logo
• See attached files
• Website: fswvanhoorne-example.eu

```html
<!DOCTYPE html>
<html lang="nl">
<head>
<meta charset="utf-8">
<title>Full Stable Works Vanhoorne – business card</title>
<link rel="stylesheet" href="https://fonts.googleapis.com/css2?family=PT+Serif:wght@400;700&display=swap">
<style>
  :root {
    --backdrop: #2a2a2c;
    --card: #141414;
    --red: #c8262b;
    --white: #f2f2f2;
    --grey: #7a7a7c;
  }
  * { margin: 0; padding: 0; box-sizing: border-box; }
  html, body {
    width: 1200px; height: 799px; overflow: hidden;
    background: var(--backdrop);
    font-family: "PT Serif", Georgia, serif;
  }
  .sheet {
    position: relative; width: 1200px; height: 799px;
    display: flex; align-items: center; justify-content: center; gap: 60px;
  }
  .card {
    position: relative; width: 510px; height: 292px;
    background: var(--card);
    box-shadow: 0 10px 30px rgba(0,0,0,.5);
    overflow: hidden;
  }
  /* back side */
  .card--back {
    display: flex; flex-direction: column; align-items: center; justify-content: center; gap: 14px;
  }
  .brand-back {
    display: flex; align-items: center; gap: 12px;
    color: var(--grey); font-weight: 700; font-size: 25px; letter-spacing: .5px;
  }
  .brand-back .mark-dot { width: 18px; height: 18px; border-radius: 50%; background: var(--grey); }
  .website-back { color: var(--grey); font-size: 14px; letter-spacing: 1px; }

  /* front side */
  .brand-front {
    position: absolute; left: 26px; top: 124px; width: 196px;
    display: flex; align-items: center; gap: 10px;
    color: var(--white); font-weight: 700; font-size: 18px; line-height: 1.2;
  }
  .brand-front .mark-dot { flex: none; width: 14px; height: 14px; border-radius: 50%; background: var(--red); }
  .divider-v { position: absolute; left: 232px; top: 34px; width: 4px; height: 196px; background: var(--red); }
  .divider-h { position: absolute; left: 232px; top: 90px; width: 210px; height: 4px; background: var(--red); }
  .person { position: absolute; left: 250px; top: 30px; }
  .person__name { color: var(--red); font-weight: 700; font-size: 21px; line-height: 1.1; }
  .person__role { color: var(--white); font-size: 12px; margin-top: 3px; }
  .company { position: absolute; left: 250px; top: 104px; color: var(--red); font-weight: 700; font-size: 15px; }
  .contacts { position: absolute; left: 250px; top: 138px; list-style: none; }
  .contacts li {
    display: flex; align-items: center; gap: 10px;
    color: var(--white); font-size: 11px; line-height: 1.35; margin-bottom: 12px;
  }
  .contacts svg { flex: none; width: 20px; height: 20px; }
  .contacts .phone, .contacts .mail { font-size: 12.5px; }
  .contacts li:last-child { margin-bottom: 0; }
</style>
</head>
<body>
<main class="sheet">
  <section class="card card--back" aria-label="Card back">
    <div class="brand-back"><span class="mark-dot"></span>Full Stable Works Vanhoorne</div>
    <p class="website-back">fswvanhoorne-example.eu</p>
  </section>

  <section class="card card--front" aria-label="Card front">
    <div class="brand-front"><span class="mark-dot"></span><span>Full Stable Works Vanhoorne</span></div>
    <div class="divider-v"></div>
    <div class="divider-h"></div>
    <div class="person">
      <p class="person__name">Gerard Vanhoorne</p>
      <p class="person__role">zaakvoerder</p>
    </div>
    <p class="company">Full Stable Works</p>
    <ul class="contacts">
      <li>
        <svg viewBox="0 0 20 20" aria-hidden="true"><path d="M10 1a6 6 0 0 0-6 6c0 4.5 6 11 6 11s6-6.5 6-11a6 6 0 0 0-6-6zm0 8.3A2.3 2.3 0 1 1 10 4.7a2.3 2.3 0 0 1 0 4.6z" fill="var(--red)"/></svg>
        <span class="address">Full Stable Works Vanhoorne GCV<br>Lindekouter 47<br>B - 9999 Voorbeeldegem België</span>
      </li>
      <li>
        <svg viewBox="0 0 20 20" aria-hidden="true"><path d="M5 2l3 3.5-1.8 2a10 10 0 0 0 6.3 6.3l2-1.8L18 15l-2 3C9 17.5 2.5 11 2 4z" fill="var(--red)"/></svg>
        <span class="phone">+ 32 400 98 76 10</span>
      </li>
      <li>
        <svg viewBox="0 0 20 20" aria-hidden="true"><rect x="2" y="4.5" width="16" height="11" fill="none" stroke="var(--red)" stroke-width="1.8"/><path d="M2.5 5l7.5 6 7.5-6" fill="none" stroke="var(--red)" stroke-width="1.8"/></svg>
        <span class="mail">gerard@fswvanhoorne-example.eu</span>
      </li>
    </ul>
  </section>
</main>
</body>
</html>
```